Dorsey K. Wendell Business Card

We need a business card for our company Dorsey K. Wendell Heating & Plumbing to be distributed to potential customers. It should follow the color scheme of our logo and have a modern upscale and masculine look.

The logo is attached and the info below should also be included:

5187 W. Cedar Brook Rd.
Fernbrook, PA 17582

Russell T. Wendell
(717) 592-0817
russelltwendell@fernmail.net
dorseykwendell.net
PA #093148

Industry/Entity Type

Business

Contact Information for Business Card

5187 W. Cedar Brook Rd.
Fernbrook, PA 17582

Russell T. Wendell
(717) 592-0817
russelltwendell@fernmail.net
dorseykwendell.net
PA #093148

Colors

Designer to choose colors to be used in the design.

Requirements
Must have
• Information above included

```html
<!DOCTYPE html>
<html lang="en">
<head>
<meta charset="utf-8">
<title>Dorsey K. Wendell Business Card</title>
<link href="https://fonts.googleapis.com/css2?family=Lato:wght@400;700&display=swap" rel="stylesheet">
<style>
  :root {
    --stage: #9e9e9e;
    --lime: #b5cc0c;
    --lime-deep: #a9be0b;
    --charcoal: #3c3c3c;
    --slate: #4a4a4a;
    --brand-blue: #1f4aa8;
    --paper: #ffffff;
  }
  html, body {
    margin: 0;
    width: 1199px;
    height: 1200px;
    overflow: hidden;
    background: var(--stage);
    font-family: "Lato", sans-serif;
  }
  .canvas { position: relative; width: 1199px; height: 1200px; }
  .card {
    position: absolute;
    left: 319px;
    width: 571px;
    height: 326px;
    border-radius: 20px;
    overflow: hidden;
  }
  .card-front { top: 225px; }
  .card-back { top: 639px; background: var(--paper); }
  .pattern-fill {
    position: absolute;
    inset: 0;
    background: linear-gradient(135deg, var(--lime) 0%, var(--lime-deep) 100%);
  }
  .brand {
    position: absolute;
    display: flex;
    align-items: center;
    gap: 10px;
    font-weight: 700;
    white-space: nowrap;
  }
  .brand-mark { width: 34px; height: 34px; }
  .brand-name { font-size: 24px; letter-spacing: 0.2px; }
  .brand-front { left: 50%; top: 163px; transform: translate(-50%, -50%); color: var(--charcoal); }
  .brand-front .brand-mark { background: var(--charcoal); }
  .brand-back { left: 54px; top: 157px; transform: translateY(-50%); color: var(--brand-blue); }
  .brand-back .brand-mark { background: var(--brand-blue); width: 30px; height: 30px; }
  .brand-back .brand-name { font-size: 21px; }
  .info-band {
    position: absolute;
    left: 300px;
    top: 0;
    width: 224px;
    height: 100%;
  }
  .holder-name {
    position: absolute;
    left: 24px;
    top: 48px;
    margin: 0;
    font-size: 18px;
    font-weight: 700;
    color: var(--charcoal);
    white-space: nowrap;
  }
  .licence {
    position: absolute;
    left: 24px;
    top: 73px;
    margin: 0;
    font-size: 12.5px;
    color: var(--slate);
  }
  .contact-list {
    position: absolute;
    left: 24px;
    top: 177px;
    margin: 0;
    padding: 0;
    list-style: none;
    font-size: 12.5px;
    color: var(--slate);
    white-space: nowrap;
  }
  .contact-list li { display: flex; align-items: flex-start; margin-bottom: 6px; line-height: 21px; }
  .contact-list svg { width: 11px; height: 11px; margin-top: 5px; margin-right: 17px; flex: none; fill: var(--brand-blue); }
</style>
</head>
<body>
<main class="canvas">
  <section class="card card-front">
    <div class="pattern-fill" role="img" aria-label="Lime background with a faint repeating pipe-work pattern"></div>
    <div class="brand brand-front">
      <span class="brand-mark"></span>
      <span class="brand-name">Dorsey K. Wendell</span>
    </div>
  </section>

  <section class="card card-back">
    <div class="brand brand-back">
      <span class="brand-mark"></span>
      <span class="brand-name">Dorsey K. Wendell</span>
    </div>
    <div class="info-band">
      <div class="pattern-fill" role="img" aria-label="Lime band with a faint repeating pipe-work pattern"></div>
      <h1 class="holder-name">Russell T. Wendell</h1>
      <p class="licence">PA #093148</p>
      <ul class="contact-list">
        <li><svg viewBox="0 0 24 24"><path d="M6.6 10.8c1.4 2.8 3.8 5.1 6.6 6.6l2.2-2.2c.3-.3.7-.4 1-.2 1.1.4 2.3.6 3.6.6.6 0 1 .4 1 1V20c0 .6-.4 1-1 1C10.6 21 3 13.4 3 4c0-.6.4-1 1-1h3.5c.6 0 1 .4 1 1 0 1.3.2 2.5.6 3.6.1.3 0 .7-.2 1z"/></svg>(717) 592-0817</li>
        <li><svg viewBox="0 0 24 24"><path d="M12 2C8.1 2 5 5.1 5 9c0 5.2 7 13 7 13s7-7.8 7-13c0-3.9-3.1-7-7-7zm0 9.5a2.5 2.5 0 1 1 0-5 2.5 2.5 0 0 1 0 5z"/></svg><span>5187 W. Cedar Brook Rd.<br>Fernbrook, PA 17582</span></li>
        <li><svg viewBox="0 0 24 24"><rect x="2" y="5" width="20" height="14"/><path d="M3 6l9 7 9-7" fill="none" stroke="#b5cc0c" stroke-width="2"/></svg>russelltwendell@fernmail.net</li>
        <li><svg viewBox="0 0 24 24"><circle cx="12" cy="12" r="10"/><path d="M2 12h20M12 2c3 3 3 17 0 20M12 2c-3 3-3 17 0 20" fill="none" stroke="#b5cc0c" stroke-width="1.5"/></svg>www.dorseykwendell.net</li>
      </ul>
    </div>
  </section>
</main>
</body>
</html>
```